RW Talbrook LLC Business Card - Civil Engineering & Consulting Firm

We need a Business Card that is elegant, and masculine.  It is our Professional Civil Engineering & Consulting Company located in San Antonio TX (Not s construction or builder firm- no gears & no tool images please). We provide civil engineering services including  commercial site plans, grading and drainage plans, utility plans, hydraulics and hydrology, land planning, utility coordination, and other general civil engineering services related to commercial and residential development.
We have 2 existing Logos. We would like to convey reliability, strength, trustworthiness and attention to detail.  Blues and orange tones as per logo We are OK with the use of a darker blue in the mix.  We have 2 logo versions - Full Company Name Logo to go on the back of card, & Small Icon Logo for the front w/ personal Info.

Target Market(s)
Architects, Real Estate Developers, Other Strctural Engineers, Surveyers, General Contractors
Industry/Entity Type
Professional Civil Engineering
Contact Information for Business Card
Name, Position, Address, Cell & Office #, email, and company website
Font styles to use
Other font styles liked:
- Avian
Requirements
Should not have
- No Tools, No Gears, no Cranes, or Construction Equipment.

```html
<!DOCTYPE html>
<html lang="en">
<head>
<meta charset="utf-8">
<title>RW Talbrook LLC Business Card</title>
<link rel="stylesheet" href="https://fonts.googleapis.com/css2?family=Montserrat:wght@400;500;700&display=swap">
<style>
  :root {
    --backdrop: #8f8f8f;
    --card: #fbfbfb;
    --orange: #ee8f2b;
    --blue: #7bafd8;
    --ink: #1c1c1c;
  }
  * { box-sizing: border-box; margin: 0; padding: 0; }
  html, body {
    width: 1160px; height: 1200px; overflow: hidden;
    background: var(--backdrop);
    font-family: "Montserrat", Arial, sans-serif;
  }
  .card {
    position: absolute; left: 199px; width: 777px; height: 442px;
    background: var(--card); border-radius: 26px; overflow: hidden;
  }
  .card--front { top: 104px; }
  .card--back { top: 634px; }

  .front-mark {
    position: absolute; left: 150px; top: 150px; width: 150px;
    text-align: center; color: var(--orange);
    font-weight: 700; font-size: 26px; line-height: 1.25; letter-spacing: 1px;
  }
  .front-mark__square {
    display: block; width: 18px; height: 18px; margin: 0 auto 14px;
    background: var(--blue);
  }
  .divider {
    position: absolute; left: 352px; top: 84px; width: 2px; height: 289px;
    background: var(--orange);
  }
  .details { position: absolute; left: 403px; top: 78px; color: var(--ink); }
  .details__name {
    color: var(--orange); font-weight: 700; font-size: 26px; letter-spacing: 0.5px;
    line-height: 1.2;
  }
  .details__role { font-size: 20px; line-height: 1.2; margin-top: 3px; }
  .details__address { font-size: 20px; line-height: 28px; margin-top: 28px; }
  .contacts { list-style: none; margin-top: 22px; }
  .contacts li {
    display: flex; align-items: center; height: 31px; font-size: 21px;
  }
  .contacts svg { width: 22px; height: 22px; margin-right: 14px; fill: var(--orange); flex: none; }

  .back-mark {
    position: absolute; left: 0; right: 0; top: 190px;
    display: flex; justify-content: center; align-items: center; gap: 18px;
  }
  .back-mark__square { width: 26px; height: 26px; background: var(--orange); }
  .back-mark__name {
    color: var(--blue); font-weight: 500; font-size: 54px; letter-spacing: 3px;
    line-height: 1;
  }
</style>
</head>
<body>
  <section class="card card--front">
    <div class="front-mark"><span class="front-mark__square"></span>RW<br>Talbrook<br>LLC</div>
    <div class="divider"></div>
    <div class="details">
      <h1 class="details__name">DANE HOLLOWAY</h1>
      <p class="details__role">Co-Founder</p>
      <p class="details__address">4180 N. Ridge Avenue<br>Suite 210 Alderton 14</p>
      <ul class="contacts">
        <li><svg viewBox="0 0 24 24" aria-hidden="true"><path d="M6.6 10.8c1.4 2.8 3.8 5.1 6.6 6.6l2.2-2.2c.3-.3.7-.4 1-.2 1.1.4 2.3.6 3.6.6.6 0 1 .4 1 1V20c0 .6-.4 1-1 1C10.6 21 3 13.4 3 4c0-.6.4-1 1-1h3.5c.6 0 1 .4 1 1 0 1.3.2 2.5.6 3.6.1.3 0 .7-.2 1l-2.3 2.2z"/></svg>412-555-0186</li>
        <li><svg viewBox="0 0 24 24" aria-hidden="true"><path d="M2 8c0-2 4-4 10-4s10 2 10 4v2h-5V8.5c-1.5-.5-3-.7-5-.7s-3.5.2-5 .7V10H2V8zm5 4 2-3h6l2 3 2 8H5l2-8zm5 1.5a2.5 2.5 0 1 0 0 5 2.5 2.5 0 0 0 0-5z"/></svg>412-555-0247</li>
        <li><svg viewBox="0 0 24 24" aria-hidden="true"><path d="M2 5h20v14H2V5zm2 2v.5l8 5.5 8-5.5V7H4zm0 3v7h16v-7l-8 5.5L4 10z"/></svg>info@rwtalbrookllc</li>
        <li><svg viewBox="0 0 24 24" aria-hidden="true"><path d="M12 2a10 10 0 1 0 0 20 10 10 0 0 0 0-20zm-1 17.9A8 8 0 0 1 4.2 10.5L9 15v1c0 1.1.9 2 2 2v1.9zm6.9-2.5c-.3-.8-1-1.4-1.9-1.4h-1v-3c0-.6-.4-1-1-1H8v-2h2c.6 0 1-.4 1-1V7h2c1.1 0 2-.9 2-2v-.4a8 8 0 0 1 2.9 12.8z"/></svg>www.talbrookcivil.com</li>
      </ul>
    </div>
  </section>

  <section class="card card--back">
    <div class="back-mark">
      <span class="back-mark__square"></span>
      <span class="back-mark__name">RW TALBROOK LLC</span>
    </div>
  </section>
</body>
</html>
```